8 page Newsletter Template Design

Please design an 8-page newsletter template that incorporates ads, index, 2 column and 3 column pages, annual theme logo and the KLTR logo.

All designs must be editable in word and in publisher for the stationary, the newsletter template and the business card template.

The business card template must be laid out in word - tolsen label 3.346 x 2.126

Back page should include contact information fields including:
Name of League
Contact Email
Contact website url
Phone Number

General font is comfortaa.

The design must be editable in two different formats: MS Word and Publisher using the color palate below.

The Blue is C90 - M30 - Y90 and K0
The Aqua is C89-M13-Y51- and K
The Font in theme logo with KLTR is Juluis Sans One
The Font for "Your Story" is Bambusa Pro

Samples of previous year's newsletter in publisher are uploaded.

Only received one design. Waiting...for at least 5 to choose from.

I paid for multiple designs and so far, have only received one. BTW, I even reached out to a previous designer, and to MF to invite this designer to the newsletter project...no response this weekend to my request until this morning.

Working women, women business owners

• Myriad Pro, or Comforta or Arial

0094D4
00A9DD
6FCCEA
C7EBF8
E9F6FB
00AB8E
00BBA5
67D7C9
C6EFE9
E9F9F6

• 8 pages - in publisher and in word incorporating the theme design and color palate
• the size should be 8 1/2 by 11 inches
• Images must be able to be changed out/revised

```html
<!DOCTYPE html>
<html lang="en">
<head>
<meta charset="utf-8">
<title>KLTR Newsletter Template</title>
<link href="https://fonts.googleapis.com/css2?family=Comfortaa:wght@400;600&family=Julius+Sans+One&family=Parisienne&display=swap" rel="stylesheet">
<style>
:root{
  --bg:#e6e6e6;
  --paper:#ffffff;
  --teal:#1f9e9a;
  --teal-dark:#138a86;
  --aqua:#00bba5;
  --aqua-soft:#bfe9e4;
  --blue:#0094d4;
  --sky:#6fccea;
  --ice:#e9f6fb;
  --ink:#2a2a2a;
  --muted:#555;
}
*{box-sizing:border-box;margin:0;padding:0}
html,body{width:903px;height:1200px;overflow:hidden;background:var(--bg)}
body{position:relative;font-family:'Comfortaa',sans-serif;color:var(--ink)}
.page{position:absolute;width:379px;height:529px;background:var(--paper);overflow:hidden}
.p-cover{left:56px;top:54px}
.p-one{left:462px;top:54px}
.p-two{left:56px;top:610px}
.p-three{left:462px;top:610px}
.abs{position:absolute}
.body{font-size:6.2px;line-height:9px;text-align:justify}
.body p{margin-bottom:9px}
.julius{font-family:'Julius Sans One',sans-serif}
.script{font-family:'Parisienne',cursive}
.photo{position:absolute}
/* cover */
.cover-wash{position:absolute;left:0;top:0;width:379px;height:130px;background:linear-gradient(160deg,#c7ebf8 0%,#e9f9f6 45%,#fff 80%)}
.issue-line{font-size:10px;color:var(--muted);left:14px;top:12px;letter-spacing:.3px}
.nl-title{left:17px;top:62px;font-size:22px;color:var(--teal)}
.theme-name{left:245px;top:78px;width:120px;text-align:center;font-size:13px;color:var(--blue);line-height:18px}
.lead-head{left:13px;top:105px;font-size:13.5px;color:var(--teal)}
.sub-head{font-size:10px;color:var(--teal);line-height:15px}
.toc{left:13px;top:346px;font-size:6.4px;line-height:10px}
.toc span{display:inline-block;width:95px;border-bottom:1px dotted #777;margin-right:2px}
/* inner pages */
.top-band{position:absolute;left:0;top:0;width:333px;height:29px;background:linear-gradient(90deg,#138a86,#3bb3ab 50%,#1f9e9a)}
.page-no{position:absolute;right:14px;top:4px;font-size:17px;color:var(--teal)}
.story-head{font-size:12px;color:var(--teal);font-weight:600}
.sidebar{position:absolute;background:var(--aqua-soft);padding:10px 11px}
.sidebar h3{font-size:7px;font-weight:600;margin-bottom:7px}
.back-head{font-size:12px;color:var(--ink);font-weight:600}
.conduct{font-size:6.2px;line-height:9px;padding-left:7px}
.conduct li{margin-bottom:0}
.footer{position:absolute;left:0;top:502px;width:379px;height:27px;background:var(--teal);color:#fff;font-size:6.3px;display:flex;align-items:center}
.footer .cell{display:flex;align-items:center;gap:5px;padding:0 10px;height:100%}
.footer .cell.alt{background:var(--aqua)}
.dot{width:10px;height:10px;border-radius:50%;background:#fff;display:inline-block}
.brand{font-size:20px;font-weight:600;color:var(--ink);display:flex;align-items:center;gap:5px}
.brand i{width:12px;height:12px;background:#d9282f;display:inline-block}
.field{font-size:6.5px}
</style>
</head>
<body>

<!-- Cover -->
<section class="page p-cover">
  <div class="cover-wash"></div>
  <div class="abs julius issue-line">DATE (MONTH YEAR) | VOL. #, ISSUE #</div>
  <div class="abs script nl-title">Newsletter Title</div>
  <div class="abs theme-name julius">RISE<br>TOGETHER</div>
  <div class="abs julius lead-head">LEAD STORY HEADLINE</div>
  <div class="abs body" style="left:13px;top:136px;width:355px">
    <p>This story can fit 125-165 words.</p>
    <p>This is greeked text for copy placement. Use this as a placeholder for text when it's not readily available.</p>
    <p>This is a layout tool intended to aid in the design process, to provide adequate amounts of copy to proof a layout and style. It's a necessary element for building good design. Greeked copy is a standard in the marketing industry. The process of greeking is no more than just applying the style to a copy block, flowing text, and printing out a comprehensive layout. A good greeked block of copy includes adequate lengths of random sentences and paragraphs.</p>
    <p>This aids in providing an accurate layout. Greeking is a formal "exercise" and not a substitute for final copy-fitting. The client should always bear in mind that greeking is a formal "exercise" and not a substitution.</p>
  </div>
  <div class="abs julius sub-head" style="left:13px;top:256px">MISSION STATEMENT OF THE KEYSTONE<br>LEAGUE OF TRADE REPRESENTATIVES</div>
  <div class="abs body" style="left:13px;top:288px;width:355px">
    <p>The mission of the Keystone League of Trade Representatives is to bring together businesswomen of diverse occupations and to provide opportunities for them to help themselves and others grow personally and professionally through leadership, education, networking support, and</p>
  </div>
  <div class="abs julius sub-head" style="left:13px;top:327px">INSIDE THIS ISSUE:</div>
  <div class="abs toc">
    <div><span>Inside Story Title</span>2</div>
    <div><span>Inside Story Title</span>2</div>
    <div><span>Inside Story Title</span>3</div>
    <div><span>Inside Story Title</span>3</div>
    <div><span>Inside Story Title</span>4</div>
    <div><span>Inside Story Title</span>4</div>
  </div>
  <svg class="abs" style="left:0;top:400px" width="379" height="129" viewBox="0 0 379 129">
    <path d="M0 65 C60 90 120 110 200 129 L0 129Z" fill="#67d7c9"/>
    <path d="M0 85 C50 105 100 120 150 129 L0 129Z" fill="#1f9e9a"/>
    <path d="M0 108 C30 118 60 125 80 129 L0 129Z" fill="#6fccea"/>
  </svg>
  <div class="photo" role="img" aria-label="Portrait photo of a smiling businesswoman holding a tablet" style="left:273px;top:392px;width:96px;height:96px;border-radius:50%;background:radial-gradient(circle at 50% 45%,#f4f4f4,#d9d9d9)"></div>
</section>

<!-- Page 01 -->
<section class="page p-one">
  <div class="top-band" role="img" aria-label="Banner photo of glass office towers in teal"></div>
  <div class="page-no">01</div>
  <div class="abs story-head" style="left:13px;top:38px">STORY HEADLINE</div>
  <div class="abs julius" style="left:240px;top:42px;font-size:6.5px;color:var(--muted)">DATE (MONTH YEAR) | VOL. #, ISSUE #</div>
  <div class="abs body" style="left:13px;top:61px;width:109px">
    <p>This story can fit 175-225 words. This is greeked text for copy placement. Neat, huh? Use this as a placeholder for text when it's not readily available. This is a layout tool. It's intended to aid in the design process, to give the designer adequate amounts of copy to proof a layout and style.</p>
    <p>Greeked copy is a standard in the marketing industry. The client has to see a concept, you have to provide text and line spacing. Greeking provides both. The process of greeking is no more than just applying the style to a copy block, flowing text, and printing out a comprehensive layout. Just imagine the time it</p>
  </div>
  <div class="abs body" style="left:131px;top:61px;width:107px">
    <p>would take for you to rewrite interesting body copy for each and every job. A good greeked block of copy includes adequate lengths of random sentences and paragraphs, much the same as a real block of final draft copy.</p>
    <p>This aids in providing an accurate layout. A greeked copy block should never become a substitution for the "look" of finished copy. The client should always bear in mind that greeking is a formal "exercise" and not a substitute for final copy-fitting. Remember, a clean and accurate copy-fitted text block is the result of careful and tedious attention to detail. It is a skill.</p>
  </div>
  <div class="sidebar body" style="left:247px;top:61px;width:120px;height:182px">
    <h3>Sidebar for News &amp; Events</h3>
    <p>This story can fit 75-125 words. Use this as a placeholder for text when it's not readily available.</p>
    <p>This is a layout tool intended to aid in the design process, to provide adequate amounts of copy to proof a layout and style.</p>
    <p>The process of greeking is no more than just applying the style to a copy block, flowing text, and printing out a comprehensive layout.</p>
  </div>
  <div class="photo" role="img" aria-label="Photo of a row of smiling professional women" style="left:0;top:265px;width:379px;height:74px;background:linear-gradient(90deg,#b7b7b7,#e2ddd6 30%,#cfc8c0 60%,#e8e8e8)"></div>
  <div class="abs story-head" style="left:13px;top:352px">STORY HEADLINE</div>
  <div class="abs body" style="left:13px;top:376px;width:355px">
    <p>This story can fit 125-165 words.</p>
    <p>This is greeked text for copy placement. Use this as a placeholder for text when it's not readily available.</p>
    <p>This is a layout tool intended to aid in the design process, to provide adequate amounts of copy to proof a layout and style. It's a necessary element for building good design. Greeked copy block, flowing text, and printing out a comprehensive layout. A good greeked block of copy includes adequate lengths of random sentences and paragraphs. This aids in providing an accurate layout. Greeking is a formal "exercise" and not a substitute for final copy-fitting. The client should always bear in mind that greeking is a formal "exercise" and not a substitution.</p>
  </div>
  <div class="photo" role="img" aria-label="Photo of business people silhouetted against a sunlit window" style="left:0;top:471px;width:379px;height:58px;background:linear-gradient(90deg,#5a4a3a,#a9876a 45%,#f3dcb8 70%,#8a6e55)"></div>
</section>

<!-- Page 02 -->
<section class="page p-two">
  <div class="top-band" role="img" aria-label="Banner photo of glass office towers in teal"></div>
  <div class="page-no">02</div>
  <div class="abs story-head" style="left:13px;top:38px">STORY HEADLINE</div>
  <div class="abs body" style="left:13px;top:61px;width:109px">
    <p>This story can fit 175-225 words. This is greeked text for copy placement. Neat, huh? Use this as a placeholder for text when it's not readily available. This is a layout tool. It's intended to aid in the design process, to give the designer adequate amounts of copy to proof a layout and style.</p>
    <p>Greeked copy is a standard in the marketing industry. The client has to see a concept, you have to provide text and line spacing. Greeking provides both. The process of greeking is no more than just applying the style to a copy block, flowing text, and printing out a comprehensive layout. Just imagine the time it</p>
  </div>
  <div class="abs body" style="left:131px;top:61px;width:107px">
    <p>would take for you to rewrite interesting body copy for each and every job. A good greeked block of copy includes adequate lengths of random sentences and paragraphs, much the same as a real block of final draft copy.</p>
    <p>This aids in providing an accurate layout. A greeked copy block should never become a substitution for the "look" of finished copy. The client should always bear in mind that greeking is a formal "exercise" and not a substitute for final copy-fitting. Remember, a clean and accurate copy-fitted text block is the result of careful and tedious attention to detail. It is a skill.</p>
  </div>
  <div class="photo" role="img" aria-label="Photo of a woman working on a laptop in a cafe" style="left:246px;top:53px;width:121px;height:143px;background:linear-gradient(160deg,#d8d2c8,#8a7563 60%,#5c4a3c)"></div>
  <div class="sidebar body" style="left:246px;top:196px;width:121px;height:304px">
    <p>This story can fit 125-175 words.</p>
    <p>This is greeked text for copy placement. Neat, huh? Use this as a placeholder for text when it's not readily available.</p>
    <p>This is a layout tool. It's intended to aid in the design process, to give the designer adequate amounts of copy to proof a layout and style.</p>
    <p>Greeked copy is a standard in the marketing industry. The client has to see a concept, you have to provide text and line spacing.</p>
    <p>The process of greeking is no more than just applying the style to a copy block, flowing text, and printing out a comprehensive layout. A good greeked block of copy includes adequate lengths of random sentences and paragraphs, much the same as a real block of final</p>
  </div>
  <div class="photo" role="img" aria-label="Double-exposure photo of a businesswoman with a city skyline at sunset" style="left:13px;top:278px;width:233px;height:92px;background:linear-gradient(90deg,#eef3f6,#c6d4dd 40%,#7f8d98 70%,#e9c79a)"></div>
  <div class="abs body" style="left:13px;top:382px;width:109px">
    <p>This story can fit 125-165 words.</p>
    <p>This is greeked text for copy placement. Use this as a placeholder for text when it's not readily available.</p>
    <p>This is a layout tool intended to aid in the design process, to provide adequate amounts of copy to proof a layout and style. It's a necessary element for building good design. Greeked copy is a standard in the</p>
  </div>
  <div class="abs body" style="left:131px;top:382px;width:107px">
    <p>copy block, flowing text, and printing out a comprehensive layout. A good greeked block of copy includes adequate lengths of random sentences and paragraphs.</p>
    <p>This aids in providing an accurate layout. Greeking is a formal "exercise" and not a substitute for final copy-fitting. The client should always bear in mind that greeking is a formal "exercise" and not a substitution.</p>
  </div>
</section>

<!-- Page 03 -->
<section class="page p-three">
  <div class="top-band" role="img" aria-label="Banner photo of glass office towers in teal"></div>
  <div class="page-no">03</div>
  <div class="abs back-head" style="left:13px;top:39px">BACK PAGE STORY HEADLINE</div>
  <div class="abs body" style="left:13px;top:63px;width:222px">
    <p>This story can fit 175-225 words. This is greeked text for copy placement. Neat, huh? Use this as a placeholder for text when it's not readily available. This is a layout tool. It's intended to aid in the design process, to give the designer adequate amounts of copy to proof a layout and style. Greeked copy is a standard in the marketing industry. The client has to see a concept, you have to provide text and line spacing. Greeking provides both. The process of greeking is no more than just applying the style to a copy block, flowing text, and printing comprehensive layout.</p>
    <p>Greeked copy is a standard in the marketing industry. You have to provide text and line spacing. Greeking provides both. The process of greeking is no more than just applying the style to a copy block, flowing text, and printing out a comprehensive layout. Just imagine the time it would take for you to rewrite interesting body copy for each and every job. A good greeked block of copy includes adequate lengths of random sentences and paragraphs, similar to a real block of final draft copy.</p>
    <p>A greeked copy block should never become a substitution for the "look" of finished copy. The client should always bear in mind that greeking is a formal "exercise" and not a substitution for final copy-fitting. Remember, a clean and accurate copy-fitted text block is the result of careful and tedious attention to detail. It is a skill.</p>
  </div>
  <div class="photo" role="img" aria-label="Black and white photo of a businesswoman on the phone" style="left:248px;top:35px;width:119px;height:141px;background:linear-gradient(150deg,#cfcfcf,#8c8c8c 55%,#e4e4e4)"></div>
  <div class="sidebar body" style="left:248px;top:176px;width:119px;height:254px;padding-top:12px">
    <p style="font-size:8.5px;line-height:12px;text-align:left">WE ARE Changing Women's Lives...</p>
    <p>This story can fit 175-225 words. This is greeked text for copy placement. Neat, huh? Use this as a placeholder for text when it's not readily available. Greeked copy is a standard in the marketing industry.</p>
    <p>The client has to see a concept, you have to provide text and line spacing. Greeking provides both. The process of greeking is no more than just applying the style to a copy block, flowing text, and printing out a layout.</p>
    <p class="script" style="font-size:11px;text-align:center;margin-top:4px">a good greeked</p>
  </div>
  <div class="abs back-head" style="left:13px;top:289px">KLTR'S PROUD CODE OF CONDUCT</div>
  <ul class="abs conduct" style="left:13px;top:308px;width:222px">
    <li>All members will serve as goodwill ambassadors for the Keystone League of Trade Representatives.</li>
    <li>Members will not allow their personal beliefs and convictions to interfere with the representation of KLTR's mission.</li>
    <li>Members will always treat their member colleagues, guests, vendors and sponsors with honesty, respect, fairness, integrity, responsibility, kindness, and in good faith.</li>
    <li>Members will maintain compliance with KLTR National, Chapter and Express Network Bylaws.</li>
    <li>Members will not use their personal power to advance their personal interests.</li>
    <li>Members will strive for excellence in their professions by maintaining and enhancing their own business knowledge and skills, and by encouraging the professional development of other members.</li>
  </ul>
  <div class="abs field" style="left:19px;top:473px">Date ______________</div>
  <div class="abs field" style="left:127px;top:473px">Time______________</div>
  <div class="abs brand" style="left:272px;top:460px"><i></i>KLTR</div>
  <footer class="footer">
    <div class="cell" style="gap:6px"><span class="dot"></span><span class="dot"></span><span class="dot"></span></div>
    <div class="cell alt">
      <svg width="9" height="9" viewBox="0 0 24 24"><path fill="#fff" d="M6.6 10.8a15 15 0 0 0 6.6 6.6l2.2-2.2c.3-.3.7-.4 1-.2 1.1.4 2.3.6 3.6.6.6 0 1 .4 1 1V20c0 .6-.4 1-1 1A17 17 0 0 1 3 4c0-.6.4-1 1-1h3.5c.6 0 1 .4 1 1 0 1.3.2 2.5.6 3.6.1.3 0 .7-.2 1z"/></svg>555-014-0199</div>
    <div class="cell">
      <svg width="9" height="9" viewBox="0 0 24 24" fill="none" stroke="#fff" stroke-width="2"><circle cx="12" cy="12" r="9"/><path d="M3 12h18M12 3c3 3 3 15 0 18M12 3c-3 3-3 15 0 18"/></svg>www.kltrnorth.org</div>
    <div class="cell alt" style="flex:1">
      <svg width="9" height="11" viewBox="0 0 24 30"><path fill="#fff" d="M12 0a10 10 0 0 0-10 10c0 8 10 20 10 20s10-12 10-20A10 10 0 0 0 12 0zm0 14a4 4 0 1 1 0-8 4 4 0 0 1 0 8z"/></svg><span style="line-height:8px">PO Box 2290, Lakeview,<br>Ohio 44012</span></div>
  </footer>
</section>

</body>
</html>
```